upmarket hair salon Double sided design flyer/A1 poster

Address
BUTLER STORE Shop 8/2 Marlowen Pde Butler 6036
Butler phone 9517 3086
YANCHEP STORE Shop 6/41 Corvella Dunes Ave Yanchep 6035
Yanchep 9538 2470
Specials
NEW Clients
Try out Silken Tressa Studio
Cut and Blow-dry
$40
Elegance Package
1/2 head of foils
or root-retouch, Cut and Blow-dry
$120*
Luxurious Package
Global Colour,Treatment,
Cut and Blow-dry
$159*
Royal Pamper Package
Colour, Foils, Treatment,
Cut and Blow-dry
$220*
*packages do not include Toners
Lavish Event Package
Event hair styling and Makeup
starting From $159
a actual Tear Off section so they can cut it out
Refer A Friend that has not been to Silken Tressa and
both Receive $20 OFF your next Colour Package
Must have the phone numbers addresses that would be in the tear of sections
Design style like
Professional
upmarket
Domask pattern
blacks whites silvers maybe gold?
colours which are in logo
if any pics must have good hair and not trashy looking girls
This is the basics will give more updates if needed

```html
<!DOCTYPE html>
<html lang="en">
<head>
<meta charset="utf-8">
<title>Silken Tressa Studio – Flyer</title>
<link rel="stylesheet" href="https://fonts.googleapis.com/css2?family=Oswald:wght@500;600&family=Open+Sans:wght@400;600;700&family=Montserrat:wght@600;700&display=swap">
<style>
  :root {
    --ink: #111111;
    --charcoal: #2a2a2c;
    --graphite: #4a4a4e;
    --silver: #c9c9cc;
    --silver-light: #efeff1;
    --white: #ffffff;
    --hair-dark: #4a2a1c;
    --hair-mid: #8a5a3c;
    --skin: #d8b39a;
  }
  * { margin: 0; padding: 0; box-sizing: border-box; }
  html, body { width: 857px; height: 1200px; overflow: hidden; background: var(--white); }
  .flyer {
    position: relative; width: 857px; height: 1200px; overflow: hidden;
    background: linear-gradient(160deg, var(--charcoal) 0%, var(--graphite) 30%, var(--silver) 62%, var(--silver-light) 80%, var(--silver) 100%);
    font-family: "Open Sans", Arial, sans-serif; color: var(--ink);
  }

  /* tear-off strip */
  .tear-strip {
    position: absolute; left: 0; top: 0; width: 165px; height: 1200px;
    background: linear-gradient(180deg, var(--ink) 0%, var(--charcoal) 55%, var(--graphite) 100%);
    border-right: 3px dashed var(--silver);
  }
  .vertical {
    position: absolute; writing-mode: vertical-rl; transform: rotate(180deg);
    white-space: nowrap;
  }
  .refer-offer {
    left: 96px; top: 18px; height: 362px;
    font-family: "Oswald", sans-serif; font-weight: 600; color: var(--white);
    text-transform: uppercase; text-align: center;
  }
  .refer-offer .line-top { display: block; font-size: 23px; line-height: 1.15; }
  .refer-offer .line-bottom { display: block; font-size: 25px; line-height: 1.15; }

  .tear-group { color: var(--silver-light); }
  .tear-group.address { left: 16px; top: 420px; height: 320px; }
  .tear-group.phone { left: 16px; top: 770px; height: 220px; }
  .tear-label {
    display: block; font-family: "Oswald", sans-serif; font-weight: 600; color: var(--white);
    font-size: 21px; letter-spacing: 1px; line-height: 1.3; margin-left: 8px;
  }
  .tear-text { display: block; font-size: 11px; line-height: 1.45; }

  .tear-brand { position: absolute; left: 20px; bottom: 40px; width: 120px; display: flex; flex-direction: column; align-items: center; gap: 6px; }
  .tear-brand .dot { width: 30px; height: 30px; border-radius: 50%; background: var(--silver); }
  .tear-brand .name { font-family: "Montserrat", sans-serif; font-weight: 600; font-size: 11px; color: var(--white); }

  /* brand */
  .brand { position: absolute; left: 200px; top: 48px; display: flex; align-items: center; gap: 12px; }
  .brand .mark { width: 44px; height: 44px; border-radius: 50%; background: var(--white); }
  .brand .name { font-family: "Montserrat", sans-serif; font-weight: 600; font-size: 28px; color: var(--white); }

  /* photos */
  .hero-photo {
    position: absolute; left: 310px; top: 0; width: 547px; height: 630px;
    background: radial-gradient(ellipse at 62% 42%, var(--skin) 0%, var(--hair-mid) 38%, var(--hair-dark) 70%, rgba(74,42,28,0) 100%);
  }
  .portrait {
    position: absolute; border-radius: 50%; border: 4px solid var(--white);
    box-shadow: 0 4px 14px rgba(0,0,0,0.4);
  }
  .portrait.one { left: 178px; top: 450px; width: 126px; height: 126px; background: radial-gradient(circle at 50% 45%, var(--skin), #c9a27a 55%, #b78b5e); }
  .portrait.two { left: 250px; top: 530px; width: 140px; height: 140px; background: radial-gradient(circle at 50% 45%, var(--skin), #3a2a22 60%, var(--ink)); }
  .portrait.three { left: 172px; top: 640px; width: 140px; height: 140px; background: radial-gradient(circle at 50% 45%, var(--skin), #6a4a34 60%, #3a2418); }

  /* address block */
  .store-address { position: absolute; left: 505px; top: 640px; width: 320px; color: var(--ink); font-size: 14px; line-height: 1.45; }
  .store-address h2 { font-family: "Oswald", sans-serif; font-weight: 600; font-size: 21px; margin-bottom: 4px; }

  /* services */
  .services-title {
    position: absolute; left: 430px; top: 798px; width: 272px; height: 56px;
    background: var(--ink); color: var(--white); border: 3px solid var(--silver-light);
    border-radius: 10px; box-shadow: 0 4px 10px rgba(0,0,0,0.45);
    font-family: "Oswald", sans-serif; font-weight: 600; font-size: 26px; letter-spacing: 1px;
    display: flex; align-items: center; justify-content: center;
  }
  .service-list { position: absolute; top: 895px; font-size: 15px; line-height: 1.32; color: var(--ink); }
  .service-list.left { left: 345px; width: 250px; }
  .service-list.right { left: 622px; width: 220px; }
  .service { margin-bottom: 20px; }
  .service .price { font-weight: 700; }
  .service .note { font-size: 13px; }
</style>
</head>
<body>
<div class="flyer">
  <div class="hero-photo" role="img" aria-label="Portrait of a woman with glossy styled auburn hair"></div>

  <aside class="tear-strip" aria-label="Tear-off contact section"></aside>

  <div class="vertical refer-offer">
    <span class="line-top">Refer to your friend and receive</span>
    <span class="line-bottom">$20 off on your colour package</span>
  </div>

  <div class="vertical tear-group address">
    <span class="tear-label">ADDRESS:</span>
    <span class="tear-text">BUTLER STORE Shop 8/2 Marlowen Pde Butler 6036<br>Butler phone 9517 3086<br>YANCHEP STORE Shop 6/41 Corvella Dunes Ave<br>Yanchep 6035</span>
  </div>

  <div class="vertical tear-group phone">
    <span class="tear-label">PHONE NO.</span>
    <span class="tear-text">Butler 9517 3086<br>Yanchep 9538 2470</span>
  </div>

  <div class="tear-brand"><span class="dot"></span><span class="name">Silken Tressa</span></div>

  <div class="brand"><span class="mark"></span><span class="name">Silken Tressa</span></div>

  <div class="portrait one" role="img" aria-label="Portrait of a woman with long blonde hair"></div>
  <div class="portrait two" role="img" aria-label="Portrait of a woman with sleek dark hair"></div>
  <div class="portrait three" role="img" aria-label="Portrait of a woman with brunette waves"></div>

  <section class="store-address">
    <h2>ADDRESS:</h2>
    <p>BUTLER STORE Shop 8/2 Marlowen Pde<br>Butler 6036 Butler phone 9517 3086<br>YANCHEP STORE Shop 6/41 Corvella Dunes Ave<br>Yanchep 6035<br>Yanchep 9538 2470</p>
  </section>

  <div class="services-title">SERVICES OFFERED</div>

  <div class="service-list left">
    <p class="service">NEW Clients: Try out Silken Tressa Studio<br>Cut and Blow-dry <span class="price">$40</span></p>
    <p class="service">Elegance Package:1/2 head of foils or root-retouch, Cut and Blow dry <span class="price">$120*</span></p>
    <p class="service">Luxurious Package:Global Colour,Treatment, Cut and Blow dry <span class="price">$159*</span></p>
  </div>
  <div class="service-list right">
    <p class="service">Royal Pamper Package: Colour, Foils, Treatment, Cut and Blow-dry <span class="price">$220*</span><br><span class="note">*packages do not include Toners</span></p>
    <p class="service">Lavish Event Package: Event hair styling and Makeup starting From <span class="price">$159</span></p>
  </div>
</div>
</body>
</html>
```